Redesign Of Flower Delivery Subscription Service Website

I need a revamped website of www.petal-rush.com

Please revamp current design using same content....

Target Market(s)

people who buy flowers. Brides, wedding planners, wedding photographer, married man, boyfriend, etc.

Industry/Entity Type

Florist

Number of Pages Required

5+ page

Colors

Designer to choose colors to be used in the design.

Requirements
Must have
• I need a revamped website of www.petal-rush.com
• Please revamp current design using same content....
Nice to have
Should not have

```html
<!DOCTYPE html>
<html lang="en">
<head>
<meta charset="utf-8">
<title>Petal Rush – Monthly Flower Delivery</title>
<link href="https://fonts.googleapis.com/css2?family=Raleway:wght@300;400;500;600&family=Lato:wght@400;700&display=swap" rel="stylesheet">
<style>
:root{
  --green:#8cc63f;
  --ink:#2b2b2b;
  --text:#555;
  --line:#d6d6d6;
  --soft-bg:#f4f4f4;
  --footer-bg:#4a4a4a;
  --footer-line:#6a6a6a;
  --white:#fff;
}
*{margin:0;padding:0;box-sizing:border-box}
html,body{width:1200px;height:3035px;overflow:hidden;background:var(--white)}
body{position:relative;font-family:"Lato",sans-serif;color:var(--text)}
.abs{position:absolute}

/* header */
.social{top:22px;left:38px;display:flex;gap:24px}
.social span{width:12px;height:12px;border-radius:50%;background:#555;display:block}
.social span.active{background:var(--green)}
.brand{top:18px;left:0;width:1200px;text-align:center}
.brand-name{font-family:"Raleway",sans-serif;font-size:34px;font-weight:500;color:#555;letter-spacing:1px}
.brand-tag{font-family:"Raleway",sans-serif;font-size:10px;color:#777;margin-top:-2px}
.tools{top:22px;right:48px;display:flex;gap:28px}
.nav{top:96px;left:0;width:1200px;display:flex;justify-content:center;gap:32px;font-family:"Raleway",sans-serif;font-size:12px;color:#444}
.nav .current{color:var(--green)}

/* hero */
.hero{top:125px;left:40px;width:1118px;height:523px;background:#f6f6f4;overflow:hidden}
.hero-photo{position:absolute;right:0;top:0;width:660px;height:523px;background:radial-gradient(ellipse at 62% 45%,#f26a2a 0%,#ee7a3c 32%,#8fbf5a 62%,rgba(246,246,244,0) 88%)}
.hero-copy{position:absolute;left:62px;top:168px}
.hero-title{font-family:"Raleway",sans-serif;font-size:40px;font-weight:400;color:var(--green);letter-spacing:.5px}
.hero-sub{font-size:13px;color:#444;margin-top:4px}
.hero-price{font-size:13px;color:#444;margin-top:2px}
.hero-price b{font-family:"Raleway",sans-serif;font-size:19px;font-weight:500;color:var(--ink);margin:0 6px}
.btn{display:inline-flex;align-items:center;gap:10px;border:1px solid #666;font-family:"Raleway",sans-serif;font-size:12px;color:#444;padding:0 18px;height:40px;background:var(--white)}
.hero .btn{margin-top:26px}

/* features */
.features{top:700px;left:40px;width:1118px;display:flex}
.feature{flex:1;display:flex;gap:16px;align-items:flex-start;padding-left:74px}
.feature+.feature{border-left:1px solid var(--line)}
.feature h3{font-family:"Raleway",sans-serif;font-weight:400;font-size:20px;color:var(--ink)}
.feature p{font-size:11px;color:#666;line-height:1.3;margin-top:4px;width:170px}

.divider{left:40px;width:1118px;height:1px;background:var(--line)}

/* services */
.section-title{left:0;width:1200px;text-align:center;font-family:"Raleway",sans-serif;font-size:28px;font-weight:400;color:var(--ink)}
.swoosh{display:block;margin:-4px auto 0}
.services{top:961px;left:40px;width:1118px;display:flex;gap:10px}
.service{width:272px;text-align:center;height:385px}
.service-photo{height:197px}
.service h4{font-family:"Raleway",sans-serif;font-weight:400;font-size:18px;color:var(--ink);margin-top:32px}
.service p{font-size:13px;color:#666;line-height:1.35;margin:6px auto 0;width:210px}
.service.featured{background:var(--white);box-shadow:0 6px 18px rgba(0,0,0,.12)}
.service .btn{margin-top:26px}

/* how it works */
.how{top:1411px;left:0;width:1200px;height:526px;background:var(--soft-bg)}
.video{position:absolute;left:42px;top:137px;width:545px;height:314px;background:#5a5a5a}
.video-bar{position:absolute;left:0;top:0;width:100%;height:40px;background:#3b3b3b;display:flex;align-items:center;gap:12px;padding-left:18px;color:#fff;font-size:17px}
.video-bar i{width:26px;height:26px;border-radius:50%;background:#c33;display:block}
.video-screen{position:absolute;left:0;top:40px;width:100%;height:236px;background:linear-gradient(#6a6a6a,#555)}
.video-controls{position:absolute;left:0;bottom:0;width:100%;height:34px;background:#222;display:flex;align-items:center;gap:14px;padding-left:18px;color:#ddd;font-size:12px}
.video-progress{position:absolute;left:0;bottom:34px;width:100%;height:4px;background:#c00}
.how-copy{position:absolute;left:612px;top:200px;width:540px}
.how-copy h3{font-family:"Raleway",sans-serif;font-size:25px;font-weight:400;color:var(--ink);white-space:nowrap}
.how-copy p{font-size:12px;line-height:1.4;color:#666;margin-top:16px;width:460px}

/* monthly */
.monthly{top:2054px;left:40px;width:540px}
.monthly h2{font-family:"Raleway",sans-serif;font-size:27px;font-weight:400;line-height:1.25;color:var(--ink)}
.monthly p{font-size:12px;line-height:1.4;color:#666;margin-top:20px;width:520px}
.monthly .btn{margin-top:36px}
.photo-yellow{top:2020px;left:648px;width:552px;height:247px;background:radial-gradient(circle at 62% 50%,#f6c21a 0%,#e69b10 28%,#2a1e06 55%,#050505 80%)}
.photo-rose{top:2093px;left:601px;width:277px;height:291px;background:var(--white);padding:4px}
.photo-rose div{width:100%;height:100%;background:radial-gradient(circle at 50% 50%,#b0224e 0%,#7a1034 45%,#1a0a10 85%)}

/* signup */
.signup-title{top:2514px;left:0;width:1200px;text-align:center;font-family:"Raleway",sans-serif;font-size:26px;color:var(--ink)}
.signup{top:2589px;left:275px;width:650px;height:54px;display:flex;border:1px solid #888}
.signup .field{flex:1;font-size:12px;font-style:italic;color:#777;display:flex;align-items:center;padding-left:20px}
.signup .submit{width:154px;background:var(--green);color:var(--white);font-family:"Raleway",sans-serif;font-size:12px;display:flex;align-items:center;justify-content:center}

/* footer */
.footer{top:2722px;left:0;width:1200px;height:313px;background:var(--footer-bg);color:#eee}
.fcol{position:absolute;top:50px}
.fcol h5{font-family:"Raleway",sans-serif;font-size:28px;font-weight:500;color:var(--white)}
.fcol p,.fcol li{font-size:12px;line-height:1.3}
.fcol ul{list-style:none;margin-top:14px}
.fcol li::before{content:"• "}
.fcol .about{margin-top:10px;width:240px}
.fcol .fsocial{display:flex;gap:28px;margin-top:42px}
.fcol .fsocial span{width:12px;height:12px;border-radius:50%;background:#999}
.fcol .fsocial span:first-child{background:var(--green)}
.contact{margin-top:14px}
.contact div{display:flex;gap:12px;font-size:12px;line-height:1.3;margin-bottom:14px}
.footer-rule{position:absolute;left:40px;top:239px;width:1118px;height:1px;background:var(--footer-line)}
.footer-bottom{position:absolute;left:40px;top:268px;width:1118px;display:flex;justify-content:space-between;font-size:11px}
</style>
</head>
<body>

<header>
  <div class="abs social"><span class="active"></span><span></span><span></span><span></span></div>
  <div class="abs brand">
    <div class="brand-name">Petal Rush</div>
    <div class="brand-tag">San Diego Flower Company</div>
  </div>
  <div class="abs tools">
    <svg width="14" height="14" viewBox="0 0 14 14"><circle cx="6" cy="6" r="4.5" fill="none" stroke="#333" stroke-width="1.6"/><path d="M9.5 9.5 13 13" stroke="#333" stroke-width="1.6"/></svg>
    <svg width="14" height="14" viewBox="0 0 14 14"><circle cx="6" cy="4.5" r="3" fill="none" stroke="#333" stroke-width="1.5"/><path d="M1 13c0-3 2.2-5 5-5s5 2 5 5" fill="none" stroke="#333" stroke-width="1.5"/><circle cx="12" cy="11" r="2" fill="var(--green)"/></svg>
    <svg width="14" height="14" viewBox="0 0 14 14"><path d="M2 4h10l-1 9H3z" fill="none" stroke="#333" stroke-width="1.5"/><path d="M5 4a2 2 0 0 1 4 0" fill="none" stroke="#333" stroke-width="1.5"/><circle cx="12" cy="12" r="2" fill="var(--green)"/></svg>
  </div>
  <nav class="abs nav">
    <span class="current">Home</span><span>How it works</span><span>Delivery areas</span><span>Franchises</span><span>Corporate arrangments</span><span>Free flowers monthly</span><span>Blog</span><span>Contact</span>
  </nav>
</header>

<section class="abs hero">
  <div class="hero-photo" role="img" aria-label="Bouquet of bright orange tulips with green leaves"></div>
  <div class="hero-copy">
    <div class="hero-title">ALWAYS FRESH</div>
    <div class="hero-sub">Beautiful Flower Arrangements Delivered Monthly</div>
    <div class="hero-price">Now only <b>$69.95/MTH</b> ($100 value)</div>
    <div class="btn">ORDER NOW <span>»</span></div>
  </div>
</section>

<section class="abs features">
  <div class="feature">
    <svg width="48" height="56" viewBox="0 0 48 56"><path d="M16 4h16v8c8 4 12 12 12 22 0 10-8 18-20 18S4 44 4 34c0-10 4-18 12-22z" fill="var(--green)"/><path d="M8 30c6-4 12 4 16 0s10-4 16 0" stroke="#fff" stroke-width="2.5" fill="none"/><path d="M8 38c6-4 12 4 16 0s10-4 16 0" stroke="#fff" stroke-width="2.5" fill="none"/></svg>
    <div><h3>FREE VASE</h3><p>Lorem Ipsum is simply dummy text of the printing industry.</p></div>
  </div>
  <div class="feature">
    <svg width="66" height="56" viewBox="0 0 66 56"><rect x="2" y="14" width="38" height="28" fill="var(--green)"/><path d="M40 22h14l10 12v8H40z" fill="var(--green)"/><circle cx="14" cy="46" r="6" fill="var(--green)" stroke="#fff" stroke-width="2"/><circle cx="52" cy="46" r="6" fill="var(--green)" stroke="#fff" stroke-width="2"/><path d="M12 28l6 6 10-12" stroke="#fff" stroke-width="3" fill="none"/></svg>
    <div><h3>FREE DELIVERY</h3><p>Lorem Ipsum is simply dummy text of the printing industry.</p></div>
  </div>
  <div class="feature">
    <svg width="50" height="58" viewBox="0 0 50 58"><path d="M25 2 48 28H34v18H16V28H2z" fill="var(--green)"/><rect x="16" y="50" width="18" height="6" fill="var(--green)"/></svg>
    <div><h3>FREE UPGRADE</h3><p>Lorem Ipsum is simply dummy text of the printing industry.</p></div>
  </div>
</section>

<div class="abs divider" style="top:840px"></div>

<div class="abs section-title" style="top:884px">OUR SERVICES
  <svg class="swoosh" width="150" height="14" viewBox="0 0 150 14"><path d="M2 10Q40 0 75 6T148 4" stroke="var(--green)" stroke-width="2" fill="none"/></svg>
</div>

<section class="abs services">
  <article class="service">
    <div class="service-photo" role="img" aria-label="Corporate banquet with pink floral centrepieces" style="background:linear-gradient(160deg,#f4ece6,#e9d6cf 50%,#d8c2b8)"></div>
    <h4>CORPORATE ARRANGMENTS</h4><p>Lorem Ipsum is simply dummy text of the printing industry.</p>
  </article>
  <article class="service featured">
    <div class="service-photo" role="img" aria-label="Hotel lobby with orchid arrangements" style="background:linear-gradient(160deg,#c99a5a,#e8c88e 45%,#f3e3c4)"></div>
    <h4>HOTEL ARRANGMENTS</h4><p>Lorem Ipsum is simply dummy text of the printing industry.</p>
    <div class="btn">READ MORE <span>»</span></div>
  </article>
  <article class="service">
    <div class="service-photo" role="img" aria-label="Event hall with white tables and tall flower displays" style="background:linear-gradient(160deg,#e9eef0,#d3dbe0 50%,#b9c6cc)"></div>
    <h4>EVENTS ARRANGMENTS</h4><p>Lorem Ipsum is simply dummy text of the printing industry.</p>
  </article>
  <article class="service">
    <div class="service-photo" role="img" aria-label="Beach wedding arch decorated with purple flowers" style="background:linear-gradient(180deg,#dfe9ee,#cfdfe5 45%,#d9c6c8 75%,#c9a8b6)"></div>
    <h4>WEDDING ARRANGMENTS</h4><p>Lorem Ipsum is simply dummy text of the printing industry.</p>
  </article>
</section>

<section class="abs how">
  <div class="abs section-title" style="top:52px">HOW IT WORKS
    <svg class="swoosh" width="150" height="14" viewBox="0 0 150 14"><path d="M2 10Q40 0 75 6T148 4" stroke="var(--green)" stroke-width="2" fill="none"/></svg>
  </div>
  <div class="video">
    <div class="video-bar"><i></i>Subscription Based Flower Deli....</div>
    <div class="video-screen" role="img" aria-label="Video thumbnail introducing the subscription service"></div>
    <div class="video-progress"></div>
    <div class="video-controls">
      <svg width="12" height="12" viewBox="0 0 12 12"><path d="M2 1v10l9-5z" fill="#ddd"/></svg>
      <svg width="14" height="12" viewBox="0 0 14 12"><path d="M1 4h3l4-3v10L4 8H1z" fill="#ddd"/></svg>
      <span>0:00/1:55</span>
    </div>
  </div>
  <div class="how-copy">
    <h3>WATCH THE VIDEOTO TO LEARN MORE</h3>
    <p>Petal Rush is a SET IT and FORGET IT subscription based flower delivery service. For an amazing price Petal Rush will hand deliver a gorgeous arrangement directly to anyone, anywhere you want, every month.</p>
    <p>When setting up your account, Petal Rush even lets you choose exact delivery dates for your Anniversary, Birthday, Valentine's and Mother's Day.</p>
    <p>Our referral program is pretty awesome too! Just refer 3 friends and each month your 3 friends pay to have flowers delivered, your flowers will be delivered free!</p>
  </div>
</section>

<section class="abs monthly">
  <h2>Monthly Subscription Based Flower<br>Delivery Service in San Diego - CA<br>by Our Florist Shop</h2>
  <p>Every moment of life could be cherished perfectly......IF you choose wisely. To make your day more treasured, remember that flowers are the smartest choice when delivered through our monthly Petal Rush subscription based delivery service. Our online subscription-based flower delivery service can help you pamper, cherish and make an everlasting impression on the minds of your loved ones with a doorstep delivery of exquisitely hand-designed floral arrangements.</p>
  <div class="btn">READ MORE <span>»</span></div>
</section>
<div class="abs photo-yellow" role="img" aria-label="Yellow lily close-up on black background"></div>
<div class="abs photo-rose"><div role="img" aria-label="Deep crimson rose close-up"></div></div>

<div class="abs divider" style="top:2449px"></div>

<div class="abs signup-title">Enter Your Email To Receive A Free Upgrade</div>
<form class="abs signup"><div class="field">Enter Your Email Address</div><div class="submit">SUBMIT NOW</div></form>

<footer class="abs footer">
  <div class="fcol" style="left:40px">
    <h5>ABOUT US</h5>
    <p class="about">Every moment of life could be cherished perfectly.......IF you choose wisely. To make your day more treasured.....</p>
    <div class="fsocial"><span></span><span></span><span></span><span></span></div>
  </div>
  <div class="fcol" style="left:380px">
    <h5>QUICK LINK</h5>
    <ul><li>Home</li><li>How it works</li><li>Delivery areas</li><li>Franchises</li><li>Corporate arrangements</li><li>Free flowers monthly</li><li>Blog</li><li>Contact</li></ul>
  </div>
  <div class="fcol" style="left:674px">
    <h5>SERVICES</h5>
    <ul><li>Corporate Arrangments</li><li>Hotel Arrangments</li><li>Events Arrangments</li><li>Wedding Arrangments</li></ul>
  </div>
  <div class="fcol" style="left:951px">
    <h5>QUICK LINK</h5>
    <div class="contact">
      <div><svg width="10" height="14" viewBox="0 0 10 14"><path d="M5 0a5 5 0 0 1 5 5c0 4-5 9-5 9S0 9 0 5a5 5 0 0 1 5-5z" fill="var(--green)"/><circle cx="5" cy="5" r="2" fill="var(--footer-bg)"/></svg><span>1840 Harbor View Road,<br>San Diego CA 92101</span></div>
      <div><svg width="12" height="10" viewBox="0 0 12 10"><rect width="12" height="10" fill="var(--green)"/><path d="M0 0l6 5 6-5" stroke="var(--footer-bg)" fill="none"/></svg><span>support@petalrushsd.com</span></div>
      <div><svg width="12" height="12" viewBox="0 0 12 12"><path d="M2 0l3 3-2 2c1 2 2 3 4 4l2-2 3 3-2 2C5 12 0 7 0 2z" fill="var(--green)"/></svg><span>619-555-0148</span></div>
    </div>
  </div>
  <div class="footer-rule"></div>
  <div class="footer-bottom"><span>© Copyright 2018 Petal Rush - All Right Reserved</span><span>Privacy Policy - Terms &amp; Conditions</span></div>
</footer>

</body>
</html>
```